Lomi-Seret - Promote and Support a community

Design a website for Ethiopean Community. the design should be friendly, easy to navigate and maintain the look & feel of the Ethiopian culture. a proposed logo is attached but it can be change according to your recommendations. This is a project we are doing at a discount rate as it supports a weak community.
Please visit their current website http://www.lomi-seret.example.il/index.php?lang=en

Target Market(s)

Community members, potential doners

Industry/Entity Type

community

Number of Pages Required

1 page

Font styles to use
Sans Serif

Requirements
Must have
• easy to navigate friendly interface

```html
<!DOCTYPE html>
<html lang="en">
<head>
<meta charset="utf-8">
<title>Lomi-Seret</title>
<link rel="stylesheet" href="https://fonts.googleapis.com/css2?family=Raleway:wght@300;400&family=Roboto:wght@300;400;700&display=swap">
<style>
:root{
  --red:#e01b22;
  --yellow:#fadf00;
  --green:#168c2e;
  --gray:#f1f1f1;
  --ink:#222;
  --text:#555;
}
*{margin:0;padding:0;box-sizing:border-box}
html,body{width:1200px;height:3526px;overflow:hidden}
body{position:relative;background:#fff;font-family:Roboto,Arial,sans-serif;color:var(--ink)}
.abs{position:absolute}
.photo{position:absolute}
.ring{position:absolute;border-radius:50%;border-style:solid}
.btn{position:absolute;display:flex;align-items:center;justify-content:center;font-weight:700;font-size:17px;text-transform:uppercase}
.btn-red{background:var(--red);color:#fff}
.btn-yellow{background:var(--yellow);color:var(--ink)}
.btn-outline{border:2px solid var(--red);color:var(--red);background:transparent}
.light{font-family:Raleway,Arial,sans-serif;font-weight:300}
.logo{position:absolute;display:flex;align-items:center;gap:8px;font-weight:700;color:var(--red);font-size:20px}
.logo .dot{width:34px;height:34px;border-radius:50%;background:var(--red)}
/* header */
.hero-panel{left:784px;top:0;width:416px;height:669px;background:var(--yellow)}
.nav{left:343px;top:69px;font-size:14px;color:#333;text-transform:uppercase}
.nav span{position:absolute;white-space:nowrap}
.topbar{top:16px;left:890px;display:flex;align-items:center;gap:6px;font-size:15px;font-weight:700}
.social{width:22px;height:22px;border-radius:50%;border:2px solid #111}
.lang{position:absolute;left:1109px;top:17px;width:44px;height:22px;border:1px solid #333;font-size:13px;display:flex;align-items:center;justify-content:center}
.welcome-line{left:47px;top:257px;width:3px;height:210px;background:var(--red)}
.hero-title{left:90px;top:262px;font-size:44px;color:#222;line-height:1}
.hero-brand{left:90px;top:320px;font-size:56px;font-weight:700;color:var(--red);line-height:1}
.arrow{font-family:Raleway,sans-serif;font-weight:300;font-size:34px;color:#555}
/* about */
.about{left:0;top:669px;width:1200px;height:888px;background:var(--gray)}
.kicker{color:var(--red);font-size:26px}
.h2{font-size:50px;line-height:60px;color:#222}
.copy{font-size:13px;line-height:21px;color:var(--text)}
.copy p{margin-bottom:21px}
/* programs */
.prog-panel{left:769px;top:1557px;width:431px;height:964px;background:var(--yellow)}
.tab{position:absolute;height:52px;color:#fff;font-family:Raleway,sans-serif;font-size:23px;display:flex;align-items:center;justify-content:center}
.card-box{position:absolute;width:256px;height:93px;border:1px solid #ddd;border-top:none;background:#fff}
.card-box p{position:absolute;left:28px;top:34px;font-size:18px;line-height:26px;color:#333;font-weight:300}
.frame{position:absolute;border:1px solid rgba(255,255,255,.6)}
/* missions */
.mission-bg{left:0;top:2521px;width:769px;height:543px;background:var(--gray)}
/* partners */
.partner{position:absolute;top:3126px;width:74px;height:58px;background:#c9c9c9;border-radius:6px}
/* footer */
.footer{left:0;top:3245px;width:1200px;height:236px;background:var(--green);color:#fff}
.f-title{font-size:22px;font-weight:700;color:var(--yellow)}
.f-text{font-size:12px;line-height:21px}
.bottom-nav{left:0;top:3481px;width:1200px;height:45px;background:var(--yellow);font-size:13px;text-transform:uppercase}
.bottom-nav span{position:absolute;top:15px}
</style>
</head>
<body>

<!-- header / hero -->
<div class="abs hero-panel"></div>
<div class="logo" style="left:52px;top:72px"><span class="dot"></span>Lomi-Seret</div>

<div class="abs topbar">
  <span class="social"></span><span class="social"></span><span class="social"></span>
  <svg width="16" height="16" viewBox="0 0 24 24" style="margin-left:18px"><path fill="#d79b00" d="M6.6 10.8a15 15 0 0 0 6.6 6.6l2.2-2.2a1 1 0 0 1 1-.3 11 11 0 0 0 3.6.6 1 1 0 0 1 1 1V20a1 1 0 0 1-1 1A17 17 0 0 1 3 4a1 1 0 0 1 1-1h3.5a1 1 0 0 1 1 1 11 11 0 0 0 .6 3.6 1 1 0 0 1-.3 1z"/></svg>
  <span>04-5550172</span>
</div>
<div class="lang">EN ▾</div>

<div class="abs nav">
  <span style="left:0">Home</span>
  <span style="left:67px">About ▾</span>
  <span style="left:141px">The Community</span>
  <span style="left:282px">Programs ▾</span>
  <span style="left:385px">News ▾</span>
  <span style="left:453px">Advocacy</span>
  <span style="left:553px">Partners</span>
</div>
<div class="btn btn-red" style="left:1000px;top:56px;width:153px;height:44px">Support us</div>

<div class="ring" style="left:377px;top:302px;width:258px;height:258px;border-width:27px;border-color:#ececec"></div>
<div class="photo" role="img" aria-label="Portrait of a woman wearing a striped shawl, outdoors with yellow flowers" style="left:501px;top:137px;width:652px;height:450px;background:linear-gradient(135deg,#7a8fa3 0%,#5a4a35 45%,#2b2118 70%,#c9b14a 100%)"></div>

<div class="abs welcome-line"></div>
<div class="abs hero-title light">WELCOME TO</div>
<div class="abs hero-brand">LOMI-SERET</div>
<div class="btn btn-yellow" style="left:90px;top:408px;width:156px;height:43px">Support us</div>
<div class="abs arrow" style="left:1108px;top:610px">‹</div>
<div class="abs arrow" style="left:1140px;top:610px">›</div>

<!-- about -->
<div class="abs about"></div>
<div class="ring" style="left:353px;top:898px;width:172px;height:172px;border-width:25px;border-color:var(--yellow)"></div>
<div class="ring" style="left:100px;top:1058px;width:168px;height:168px;border-width:24px;border-color:var(--green)"></div>
<div class="ring" style="left:309px;top:1310px;width:168px;height:168px;border-width:24px;border-color:var(--red)"></div>
<div class="photo" role="img" aria-label="Three smiling girls, one wearing a red cap" style="left:74px;top:748px;width:320px;height:398px;background:linear-gradient(160deg,#4a5560,#8a5a44 50%,#c9b9a8)"></div>
<div class="photo" role="img" aria-label="Child standing on a rocky hilltop above a green valley" style="left:212px;top:1059px;width:315px;height:358px;background:linear-gradient(180deg,#c7cfd2 0%,#8a9a7c 45%,#4f6a3e 75%,#8a7e6a 100%)"></div>

<div class="abs kicker light" style="left:620px;top:758px">WELCOME</div>
<div class="abs h2 light" style="left:620px;top:793px">Small Actions Lead<br>To Big changes</div>
<div class="abs copy" style="left:620px;top:938px;width:495px">
  <p>Aliyah (immigration) from Ethiopia to Israel and the transition to a sedentary lifestyle has resulted in the emergence of chronic diseases, in particular diabetes. While only 0.4% of the new immigrants were diagnosed with Type 2 diabetes upon arrival, by the time they had lived in Israel for ten years the figure had risen to 18% - three times as many as in the general population. The incidence of hypertension, obesity, asthma and Type 1 diabetes had also increased dramatically.</p>
  <p>Lomi Seret was founded in 1999 by Dr. Noa Lavie, Head of the Endocrinology Unit at the Harel Valley Medical Center. Her experience with Ethiopian patients made her realize that medical treatment could not succeed without culturally competent communication. Lomi Seret has developed into a small but dedicated NGO, delivering services throughout Israel with the backing and cooperation of a wide range of local and national bodies, including the Ministry of Health, the Ministry of Immigration, the absorption services, municipalities, the HMOs and hospitals.</p>
  <p>Today the Lomi Seret team comprises eight Ethiopian-Israeli healthcare professionals, three Amharic-speaking medical interpreters and four health promotion specialists familiar with the Ethiopian immigrant community. Organizations within Israel and beyond now look to Lomi Seret's programs for inspiration in their efforts to develop meaningful prevention strategies for improving the health of immigrants and minority communities.</p>
</div>
<div class="btn btn-outline" style="left:620px;top:1413px;width:150px;height:45px">Support us</div>

<!-- programs -->
<div class="abs prog-panel"></div>
<div class="tab" style="left:47px;top:1614px;width:201px;background:var(--red)">Our Programs</div>
<div class="tab" style="left:260px;top:1614px;width:187px;background:var(--green)">Latest News</div>

<div class="card-box" style="left:66px;top:1922px"><p>Health &amp; Education<br>Presentations</p></div>
<div class="photo" role="img" aria-label="Audience of community elders seated at a presentation" style="left:47px;top:1713px;width:295px;height:209px;background:linear-gradient(135deg,#6b3a3a,#d9d2c8 60%,#8a6d55)"><div class="frame" style="left:20px;top:20px;right:20px;bottom:0"></div></div>
<div class="card-box" style="left:411px;top:1922px"><p>Regional Health Fairs</p></div>
<div class="photo" role="img" aria-label="Health worker testing visitors at a health fair table" style="left:391px;top:1713px;width:296px;height:209px;background:linear-gradient(135deg,#d8d8d8,#6a5a4c 55%,#3a3a5a)"><div class="frame" style="left:20px;top:20px;right:20px;bottom:0"></div></div>

<div class="card-box" style="left:66px;top:2275px"><p>Nutrition &amp; Cookery<br>Courses</p></div>
<div class="photo" role="img" aria-label="Women sharing a meal at a cookery course" style="left:47px;top:2064px;width:295px;height:211px;background:linear-gradient(135deg,#3f6b6a,#3fa3b5 45%,#d9c9a4)"></div>
<div class="card-box" style="left:411px;top:2275px"><p>Training on Cultural<br>Competence</p></div>
<div class="photo" role="img" aria-label="Group of women at a cultural competence training session" style="left:391px;top:2064px;width:296px;height:211px;background:linear-gradient(135deg,#e4e0d8,#9a7c6a 55%,#7a3a3a)"></div>

<div class="btn btn-outline" style="left:47px;top:2416px;width:154px;height:42px">View all</div>
<div class="abs arrow" style="left:643px;top:2415px">‹</div>
<div class="abs arrow" style="left:673px;top:2415px">›</div>

<div class="abs h2 light" style="left:814px;top:1603px;line-height:58px">Health &amp; The<br>Ethiopian<br>Israeli<br>Community</div>
<div class="photo" role="img" aria-label="Portrait of an elderly man in a dark knit cap" style="left:815px;top:1876px;width:338px;height:491px;background:linear-gradient(160deg,#6a6a62,#2a2a30 50%,#3e4a5a)"><div class="frame" style="left:35px;top:35px;right:35px;bottom:35px"></div></div>
<div class="btn btn-red" style="left:908px;top:2416px;width:155px;height:44px">Support us</div>

<!-- missions -->
<div class="abs mission-bg"></div>
<div class="ring" style="left:48px;top:2558px;width:164px;height:164px;border-width:22px;border-color:var(--yellow)"></div>
<div class="ring" style="left:-62px;top:2811px;width:124px;height:124px;border-width:18px;border-color:var(--green)"></div>
<div class="ring" style="left:563px;top:2854px;width:160px;height:160px;border-width:22px;border-color:var(--red)"></div>
<div class="photo" role="img" aria-label="Children in yellow headscarves looking at something together" style="left:96px;top:2617px;width:578px;height:349px;background:linear-gradient(90deg,#d9b830,#e8e2d4 40%,#b8a89a 60%,#e0c22a)"><div class="frame" style="left:30px;top:25px;right:30px;bottom:25px"></div></div>

<div class="abs h2 light" style="left:815px;top:2606px">Our Missions<br>&amp; Goals</div>
<div class="abs copy" style="left:816px;top:2744px;width:320px">
  <p><b>Lomi Seret</b> ("health" in both Amharic and Hebrew) is dedicated to improving the health of the Ethiopian Israeli community, and firmly believes in the right of every Israeli citizen to access proper health care.</p>
  <p><b>Lomi Seret</b> believes that fostering an informed, active health leadership from within the community itself is key to achieving its goals.</p>
  <p style="color:#222;font-weight:700">Read More...</p>
</div>

<!-- partners -->
<div class="partner" style="left:68px"></div>
<div class="partner" style="left:226px"></div>
<div class="partner" style="left:388px"></div>
<div class="partner" style="left:553px"></div>
<div class="partner" style="left:713px"></div>
<div class="partner" style="left:874px"></div>
<div class="partner" style="left:1040px"></div>

<!-- footer -->
<div class="abs footer"></div>
<div class="logo" style="left:48px;top:3330px;color:#fff;font-size:18px"><span class="dot" style="background:#fff"></span>Lomi-Seret</div>
<div class="abs f-text" style="left:48px;top:3414px;font-size:11px;color:#fff">COPYRIGHT © 2022</div>

<div class="abs f-title" style="left:248px;top:3288px">Lomi Seret</div>
<div class="abs f-text" style="left:248px;top:3322px;width:270px;color:#fff">Lomi Seret means health in Amharic and also signifies a jewel basket: an expensive and unique gift to preserve.<br><b>Seret</b> means health in Hebrew.<br><b>Health is a gift to be preserved</b></div>

<div class="abs f-title" style="left:580px;top:3288px">About Us</div>
<div class="abs f-text" style="left:580px;top:3322px;width:270px;color:#fff">Lomi Seret ("health" in both Amharic and Hebrew) is dedicated to improving the health of the Ethiopian Israeli community.<br><b>Read More...</b></div>

<div class="abs f-title" style="left:914px;top:3288px">Contact</div>
<div class="abs f-text" style="left:914px;top:3326px;color:#fff">
  <div>📍&nbsp; Tamar 8/4 POB 1204 Givon, 40120</div>
  <div>✉&nbsp; lomiseret@mail.example</div>
  <div style="font-weight:700;font-size:13px">☎&nbsp; 04-5550172</div>
</div>
<div class="abs" style="left:914px;top:3412px;display:flex;gap:8px">
  <span class="social" style="border-color:#fff;width:24px;height:24px"></span>
  <span class="social" style="border-color:#fff;width:24px;height:24px"></span>
  <span class="social" style="border-color:#fff;width:24px;height:24px"></span>
</div>

<div class="abs bottom-nav">
  <span style="left:279px">Home</span>
  <span style="left:350px">About</span>
  <span style="left:427px">The Community</span>
  <span style="left:571px">Programs</span>
  <span style="left:676px">News</span>
  <span style="left:747px">Advocacy</span>
  <span style="left:850px">Partners</span>
</div>

</body>
</html>
```